Company brochure for Cedarline Stride Works, Inc.

We need a company brochure that lets referral sources know who we are, where are locations are and what services we offer. Our website is www.cedarlinestrideinc.com and we are on Facebook and Instagram. We need the brochure to feature both braces and prosthetics.

```html
<!DOCTYPE html>
<html lang="en">
<head>
<meta charset="utf-8">
<title>Cedarline Stride Works – Company Brochure</title>
<link rel="stylesheet" href="https://fonts.googleapis.com/css2?family=Playfair+Display:wght@800;900&family=Arimo:ital,wght@0,400;0,700;1,400&display=swap">
<style>
  :root{
    --blue:#2a63b8;
    --blue-dark:#1d4a94;
    --navy:#1f3f8a;
    --orange:#e8541e;
    --ink:#1b1b1b;
    --page:#ffffff;
    --fold:#e9e9ec;
    --stage:#eceef1;
  }
  *{box-sizing:border-box;margin:0;padding:0}
  html,body{width:1200px;height:1200px;overflow:hidden;background:var(--stage)}
  body{position:relative;font-family:"Arimo",Arial,sans-serif;color:var(--ink)}
  .sheet{position:absolute;left:230px;width:740px;height:575px;background:var(--page);overflow:hidden;box-shadow:0 4px 14px rgba(0,0,0,.18)}
  .sheet--outside{top:17px}
  .sheet--inside{top:608px}
  .fold{position:absolute;top:0;height:100%;width:247px}
  .fold--mid{left:247px;background:linear-gradient(90deg,#f3f3f5 0%,#fff 30%,#fff 80%,#ececef 100%)}
  .fold--right{left:493px;background:linear-gradient(90deg,#ececef 0%,#fff 25%)}
  .waves{position:absolute;left:0;top:0;width:740px;height:575px;z-index:2}
  .layer{position:absolute;z-index:3}
  .photo{position:absolute;z-index:1}

  /* About panel */
  .about-title{left:52px;top:10px;font:900 21px "Playfair Display",Georgia,serif;letter-spacing:.5px}
  .about-mark{left:28px;top:16px;width:4px;height:12px;background:var(--blue)}
  .about-lead{left:52px;top:41px;width:183px;font-size:6.3px;line-height:8.6px;text-align:justify}
  .spine{position:absolute;left:30px;top:28px;width:1px;height:395px;background:var(--orange);z-index:3}
  .hex{position:absolute;left:17px;width:27px;height:30px;z-index:4}
  .service{position:absolute;left:51px;width:184px;z-index:4}
  .service h3{font:700 10px "Arimo",Arial,sans-serif;color:var(--navy);margin-bottom:6px}
  .service p{font-size:6.3px;line-height:8.6px;text-align:justify}
  .web-light{left:40px;top:503px;font:700 8.6px "Arimo",Arial,sans-serif;color:#fff;letter-spacing:.5px;white-space:nowrap}

  /* Locations panel */
  .loc-frame{left:271px;top:56px;width:194px;height:345px;border:1.2px solid var(--orange);border-bottom:none}
  .loc-pin{left:356px;top:45px;width:24px;height:24px}
  .loc-list{left:271px;top:74px;width:194px;text-align:center}
  .loc{margin-bottom:13.5px}
  .loc h4{font:700 7.6px "Arimo",Arial,sans-serif;color:var(--orange);margin-bottom:5px}
  .loc p{font-size:6.2px;line-height:8.4px}
  .brand-mid{left:247px;top:468px;width:246px;text-align:center}
  .brand-name{font:700 11px "Arimo",Arial,sans-serif;color:var(--navy)}
  .brand-web{font:700 9.5px "Arimo",Arial,sans-serif;color:var(--orange);letter-spacing:.6px;margin-top:14px}

  /* Cover panel */
  .cover-brand{left:493px;top:60px;width:247px;text-align:center}
  .cover-brand .dot{display:inline-block;width:46px;height:46px;border-radius:50%;background:var(--navy);margin-bottom:12px}
  .cover-brand .brand-name{font-size:12px}
  .cover-text{left:493px;top:428px;width:247px;text-align:center;color:#fff}
  .cover-text h1{font:900 19px "Playfair Display",Georgia,serif;line-height:22px}
  .cover-text h2{font:900 14px "Playfair Display",Georgia,serif;line-height:18px}
  .cover-text p{font-size:11.5px;line-height:15px;margin-top:3px}
  .pill{display:inline-block;margin-top:12px;background:var(--orange);color:#fff;border-radius:10px;padding:4px 12px;font:700 9.5px "Arimo",Arial,sans-serif;letter-spacing:.6px}

  /* Inside: story panel */
  .story-bg{left:0;top:0;width:248px;height:575px;background:linear-gradient(180deg,#dfe0e0 0%,#ecebea 45%,#e6e6e4 100%)}
  .story-title{left:0;top:14px;width:248px;text-align:center;font:900 19.5px "Playfair Display",Georgia,serif;color:var(--orange);line-height:26px;letter-spacing:.5px}
  .story-rule{left:104px;top:74px;width:42px;height:3px;background:var(--orange)}
  .story-lead{left:26px;top:88px;width:203px;font-size:9.3px;line-height:12.2px;text-align:justify}
  .quote-box{left:34px;top:194px;width:190px;height:113px;border-top:1.2px solid var(--orange);border-right:1.2px solid var(--orange);border-bottom:none}
  .quote-box::after{content:"";position:absolute;right:-1px;bottom:0;width:18px;border-bottom:1.2px solid var(--orange)}
  .quote-open,.quote-close{font:900 40px "Playfair Display",Georgia,serif;color:var(--orange);line-height:1}
  .quote-open{left:32px;top:176px}
  .quote-close{left:176px;top:290px}
  .quote-text{left:34px;top:210px;width:176px;font:italic 11.8px/15.3px "Arimo",Arial,sans-serif}
  .portrait{left:80px;top:320px;width:130px;height:245px;border-radius:40px 40px 10px 10px;background:linear-gradient(180deg,#b7b3ac 0%,#6e6458 45%,#4a4a52 100%);opacity:.85}

  /* Inside: services */
  .shelf{left:248px;top:0;width:492px;height:205px;background:linear-gradient(120deg,#cfd0c8 0%,#ecece6 35%,#6f8a84 70%,#e8e4dc 100%);clip-path:path('M0,0 H492 V126 C420,175 330,205 250,201 C150,198 60,170 0,141 Z')}
  .item{position:absolute;text-align:center;z-index:4}
  .item > svg{display:block;margin:0 auto}
  .item h5{font:700 10.5px "Arimo",Arial,sans-serif;color:var(--navy);margin-top:6px}
  .item p{font-size:8.4px;line-height:17px}
  .ticks{list-style:none;text-align:left;display:inline-block;margin-top:3px}
  .ticks li{font-size:8.4px;line-height:15px;display:flex;align-items:center;gap:6px;white-space:nowrap}
  .ticks svg{flex:none;margin:0}
</style>
</head>
<body>
<svg width="0" height="0" style="position:absolute" aria-hidden="true">
  <symbol id="hex-tick" viewBox="0 0 30 33">
    <polygon points="15,0 30,8 30,25 15,33 0,25 0,8" fill="#e8541e"/>
    <rect x="8" y="12" width="14" height="9" rx="2" fill="none" stroke="#fff" stroke-width="1.4"/>
    <polyline points="10.5,15.5 14,19 20,13" fill="none" stroke="#fff" stroke-width="1.8" stroke-linecap="round" stroke-linejoin="round"/>
  </symbol>
  <symbol id="mini-tick" viewBox="0 0 10 10">
    <circle cx="5" cy="5" r="4" fill="none" stroke="#e8541e" stroke-width="1"/>
    <polyline points="3,5 4.6,6.6 7.4,3.6" fill="none" stroke="#e8541e" stroke-width="1.1"/>
  </symbol>
  <symbol id="hex-plain" viewBox="0 0 27 30">
    <polygon points="13.5,0 27,7.5 27,22.5 13.5,30 0,22.5 0,7.5" fill="#e8541e"/>
  </symbol>
</svg>

<!-- Outside spread -->
<section class="sheet sheet--outside">
  <div class="fold fold--mid"></div>
  <div class="fold fold--right"></div>
  <div class="photo" style="left:493px;top:130px;width:247px;height:310px;background:linear-gradient(160deg,#eef1f5 0%,#e8d3b8 40%,#3b5fb0 58%,#e6d6bf 75%,#f3f3f5 100%)" role="img" aria-label="Photo of knee braces and supports displayed on leg forms"></div>

  <svg class="waves" viewBox="0 0 740 575" aria-hidden="true">
    <path d="M0,395 C70,445 160,460 225,425" fill="none" stroke="#e8541e" stroke-width="2"/>
    <path d="M0,405 C60,450 155,470 230,430 C300,388 340,355 400,365 C450,375 475,420 470,480 C440,432 380,412 330,425 C270,440 230,545 0,550 Z" fill="#2a63b8"/>
    <path d="M493,432 C590,440 680,405 740,335 L740,520 C680,555 600,562 493,552 Z" fill="#2a63b8"/>
    <path d="M590,432 C660,425 710,390 740,326" fill="none" stroke="#e8541e" stroke-width="2"/>
    <path d="M575,566 C640,562 700,548 740,523" fill="none" stroke="#e8541e" stroke-width="2"/>
  </svg>

  <!-- About panel -->
  <div class="layer about-mark"></div>
  <h2 class="layer about-title">ABOUT US</h2>
  <p class="layer about-lead">Cedarline Stride Works has been providing quality, compassionate care to residents of Cedar Valley and the Riverlands since 1983. A recognized leader in the field, our experts work as a team to create the most functional solution to your orthotic, prosthetic and pedorthic needs using the latest technology available.</p>
  <div class="spine"></div>

  <svg class="hex" style="top:96px" viewBox="0 0 27 30" aria-hidden="true"><use href="#hex-plain"/><circle cx="13.5" cy="15" r="6" fill="none" stroke="#fff" stroke-width="1.2"/><circle cx="13.5" cy="15" r="2.5" fill="none" stroke="#fff" stroke-width="1.2"/></svg>
  <div class="service" style="top:105px"><h3>Our Mission</h3><p>We are people committed to using every scientific and technical development available to restore the physical capabilities of the disabled.</p></div>

  <svg class="hex" style="top:152px" viewBox="0 0 27 30" aria-hidden="true"><use href="#hex-plain"/><path d="M9,10 C9,17 12,20 18,21 L19,18 L16,17 L15,18 C13,17 12,16 11,14 L12,13 L11,10 Z" fill="none" stroke="#fff" stroke-width="1"/></svg>
  <div class="service" style="top:161px"><h3>Emergency 24/7 Service</h3><p>Our staff is available 24 hours a day, 7 days a week for emergencies that cannot wait until the next business day. At Cedarline, we are dedicated to providing the very best patient experience.</p></div>

  <svg class="hex" style="top:218px" viewBox="0 0 27 30" aria-hidden="true"><use href="#hex-plain"/><rect x="10" y="9" width="7" height="12" rx="2" fill="none" stroke="#fff" stroke-width="1.1"/></svg>
  <div class="service" style="top:227px"><h3>Prosthetic Services</h3><p>There are approximately 2 million people living with limb loss in the United States. Most limb loss occurs in those with compromised vascular systems, frequently because of complications from diabetes. Other causes of limb loss include cancer, traumatic injuries, or congenital disorders.</p></div>

  <svg class="hex" style="top:299px" viewBox="0 0 27 30" aria-hidden="true"><use href="#hex-plain"/><ellipse cx="11" cy="15" rx="2.6" ry="6" fill="none" stroke="#fff" stroke-width="1"/><ellipse cx="16.5" cy="15" rx="2.6" ry="6" fill="none" stroke="#fff" stroke-width="1"/></svg>
  <div class="service" style="top:308px"><h3>Orthotic Services</h3><p>After receiving a prescription from your physician for an orthopedic brace, you will most likely be referred to an orthotist, orthotic company or clinic team.</p></div>

  <svg class="hex" style="top:356px" viewBox="0 0 27 30" aria-hidden="true"><use href="#hex-plain"/><circle cx="13.5" cy="15" r="6" fill="none" stroke="#fff" stroke-width="1.4" stroke-dasharray="2 1.2"/><circle cx="13.5" cy="15" r="2.4" fill="#fff"/></svg>
  <div class="service" style="top:365px"><h3>Board Accredited Facility</h3><p>Did you know that in most states there are no requirements for education, certification or licensure for orthotists, prosthetists or pedorthists? Take a proactive approach in determining who you will be working with - being informed will only help you gain a positive outcome.</p></div>

  <div class="layer web-light">www.cedarlinestrideinc.com</div>

  <!-- Locations panel -->
  <div class="layer loc-frame"></div>
  <svg class="layer loc-pin" viewBox="0 0 24 24" aria-hidden="true">
    <polygon points="12,1 22,6.5 22,17.5 12,23 2,17.5 2,6.5" fill="#e8541e"/>
    <path d="M12,6.5 A3.6,3.6 0 0 1 15.6,10.1 C15.6,13 12,17 12,17 C12,17 8.4,13 8.4,10.1 A3.6,3.6 0 0 1 12,6.5 Z" fill="#fff"/>
    <circle cx="12" cy="10.1" r="1.3" fill="#e8541e"/>
  </svg>
  <div class="layer loc-list">
    <div class="loc"><h4>Main Lab and Central Fabrication Facility:</h4><p>412 Alder Row<br>Cedar Falls, ST 40118-2210</p></div>
    <div class="loc"><h4>Northgate Patient Care Center:</h4><p>Center for Mobility Care<br>2150 Linden Court, Suite 8B<br>Cedar City, ST 40122</p></div>
    <div class="loc"><h4>West County Patient Care Center:</h4><p>905 W. Harbor Lane, Suite 210 East<br>Cedar City, ST 40131</p></div>
    <div class="loc"><h4>Riverlands Patient Care Center:</h4><p>18 Willow Terrace, Suite 3<br>Brookhaven, ST 40276</p></div>
    <div class="loc"><h4>Maplecrest Patient Care Center:</h4><p>7740 Maplecrest Drive, Ste. 140<br>Fairmont, ST 40154</p></div>
    <div class="loc"><h4>Central Billing Address for all Locations:</h4><p>412 Alder Row<br>Cedar Falls, ST 40118</p></div>
  </div>
  <div class="layer brand-mid">
    <div class="brand-name">Cedarline Stride Works, Inc.</div>
    <div class="brand-web">www.cedarlinestrideinc.com</div>
  </div>

  <!-- Cover panel -->
  <div class="layer cover-brand">
    <span class="dot"></span>
    <div class="brand-name">Cedarline Stride Works, Inc.</div>
  </div>
  <div class="layer cover-text">
    <h1>Welcome to</h1>
    <h2>Cedarline Stride Works</h2>
    <p>Where we create custom made<br>solutions that work for you!</p>
    <span class="pill">www.cedarlinestrideinc.com</span>
  </div>
</section>

<!-- Inside spread -->
<section class="sheet sheet--inside">
  <div class="fold fold--mid"></div>
  <div class="fold fold--right"></div>
  <div class="photo story-bg" role="img" aria-label="Soft, faded outdoor background photo"></div>
  <div class="photo shelf" role="img" aria-label="Photo of foot orthoses, ankle braces and prosthetic feet on a clinic shelf"></div>

  <svg class="waves" viewBox="0 0 740 575" aria-hidden="true">
    <path d="M248,141 C300,168 360,190 420,198" fill="none" stroke="#e8541e" stroke-width="5"/>
    <path d="M575,195 C640,185 700,160 740,126" fill="none" stroke="#e8541e" stroke-width="5"/>
    <path d="M0,500 C70,488 150,468 205,468 C240,468 265,478 280,490 C200,500 130,540 95,575 L0,575 Z" fill="#2a63b8"/>
    <path d="M95,575 C140,535 210,500 280,490" fill="none" stroke="#e8541e" stroke-width="2"/>
    <path d="M290,575 C450,575 560,572 645,548 C705,530 732,495 740,452 L740,575 Z" fill="#2a63b8"/>
    <path d="M250,575 C420,572 540,566 640,543" fill="none" stroke="#e8541e" stroke-width="1.5"/>
  </svg>

  <h2 class="layer story-title">MOVE NATURALLY<br>SAFETY</h2>
  <div class="layer story-rule"></div>
  <p class="layer story-lead">After 32 years of trips and falls as an amputee, Dale Marsh learned to avoid certain terrain - like ramps, grass and mulch - whenever possible. But things changed the day Dale switched to TERRASTEP KNEE. Now, he says,</p>
  <div class="layer quote-box"></div>
  <div class="layer quote-open">“</div>
  <p class="layer quote-text">I don't really think about the terrain I'm walking on. It's not an issue. I feel so safe walking on TERRASTEP KNEE that I am more active than I have been in decades.</p>
  <div class="layer quote-close">”</div>
  <div class="layer portrait" role="img" aria-label="Photo of a smiling man walking outdoors with a prosthetic leg"></div>

  <div class="item" style="left:310px;top:228px;width:100px">
    <svg width="28" height="31" aria-hidden="true"><use href="#hex-tick"/></svg><h5>Cranial</h5>
  </div>
  <div class="item" style="left:310px;top:307px;width:100px">
    <svg width="28" height="31" aria-hidden="true"><use href="#hex-tick"/></svg><h5>Cervical</h5>
  </div>
  <div class="item" style="left:300px;top:388px;width:120px">
    <svg width="28" height="31" aria-hidden="true"><use href="#hex-tick"/></svg><h5>Spinal</h5>
    <ul class="ticks" style="margin-top:2px">
      <li style="line-height:13px"><svg width="7" height="7" aria-hidden="true"><use href="#mini-tick"/></svg>Spinal/Thoracic</li>
      <li style="line-height:13px"><svg width="7" height="7" aria-hidden="true"><use href="#mini-tick"/></svg>Spine/Scoliosis</li>
    </ul>
  </div>

  <div class="item" style="left:540px;top:226px;width:140px">
    <svg width="28" height="31" aria-hidden="true"><use href="#hex-tick"/></svg><h5>Upper Extremity</h5>
    <p style="margin-top:1px">Wrist Hand Orthoses<br>Shoulder-Elbow Orthoses</p>
  </div>
  <div class="item" style="left:540px;top:332px;width:140px">
    <svg width="28" height="31" aria-hidden="true"><use href="#hex-tick"/></svg><h5>Pediatric Corrective</h5>
  </div>
  <div class="item" style="left:530px;top:405px;width:160px">
    <svg width="28" height="31" aria-hidden="true"><use href="#hex-tick"/></svg><h5>Lower Extremity Orthosis</h5>
    <ul class="ticks">
      <li><svg width="7" height="7" aria-hidden="true"><use href="#mini-tick"/></svg>Foot Orthotics</li>
      <li><svg width="7" height="7" aria-hidden="true"><use href="#mini-tick"/></svg>Ankle Foot Orthoses (AFO)</li>
      <li><svg width="7" height="7" aria-hidden="true"><use href="#mini-tick"/></svg>Knee Ankle Foot Orthoses</li>
      <li><svg width="7" height="7" aria-hidden="true"><use href="#mini-tick"/></svg>Hip Orthoses</li>
    </ul>
  </div>
</section>
</body>
</html>
```